Horse-Related Social Media Web Design

Need a social media web design for the world’s largest horse training program, Brindlecott Open Equitation. The site features social media components along with educational material and videos with a free downloadable app for horse owners on-the-go. Although members receive a free 30-day membership, they must choose from three levels of membership when they sign up (similar to kinloreva.com). The original design was based off of glimmerdock.com.

We would like a mash-up of the sign-up page for Chatterlume and Quibbly. The home page will feature an intro video, sign-up field and a tag line and sub text such as:
Ready to Connect?
Connect with your horse, yourself, Brindlecott members and friends you haven’t yet met.

The final design should communicate a hip, trendy site for horse-minded people.

We need the design only, sliced for the website. We will do all coding ourselves.

The current website is www.brindlecottlink.com.

Project Deadline Extended
Reason: We've had multiple designers accept the project, but none have submitted designs.

The deadline of our project has been extended, we have guaranteed it and the budget has been raised to $1,250 US.  

We are looking forward to some excellent submissions!
Thank you.

Please think outside the box. The submissions we've received so far look much like our current site. While we would like a clean, simple look, it should also be trendy and convey that the site is fun without implicitly saying so. We will be tailoring down the text and information on the front page and placing the majority of information inside the information pages in the navigation.

Thank you!

Thank you to everyone who has participated in submitting designs for our contest. 

Target Market(s)

Target market is horse owners and lovers across the world. The company has a very international market with campuses in the UK and Australia and followers literally across the world.

Industry/Entity Type

Training

Requirements
Nice to have
• Please explain why you made certain design choices from a useability perspective when you submit the design.

```html
<!DOCTYPE html>
<html lang="en">
<head>
<meta charset="utf-8">
<title>Brindlecott Open Equitation — Connect</title>
<link href="https://fonts.googleapis.com/css2?family=Noto+Serif&family=Noto+Sans&display=swap" rel="stylesheet">
<style>
  :root{
    --page-bg:#c4c8c9;
    --panel-bg:#d4d7d8;
    --navy:#0d3a66;
    --navy-soft:#1c4a78;
    --body-text:#4a4c4e;
    --rule-light:#e4e6e7;
    --rule-dark:#8e9294;
    --frame:#f4f5f5;
    --accent-orange:#e4602a;
    --link-rust:#b3471b;
  }
  *{margin:0;padding:0;box-sizing:border-box}
  html,body{width:1200px;height:900px;overflow:hidden}
  body{background:var(--page-bg);position:relative;font-family:"Noto Sans",sans-serif;color:var(--body-text)}
  .abs{position:absolute}

  .photo{border:3px solid var(--frame);box-shadow:0 1px 2px rgba(0,0,0,.25)}
  .photo-fun{background:radial-gradient(ellipse at 35% 55%,#d9c2a0 0,#b89a70 40%,transparent 70%),radial-gradient(ellipse at 80% 50%,#6e4a2e 0,#8a6444 45%,transparent 75%),linear-gradient(90deg,#a58d68,#c4ad8a 50%,#8fa9bf)}
  .photo-learning{background:radial-gradient(ellipse at 60% 65%,#e6e2da 0,#cdbfa5 30%,transparent 60%),linear-gradient(180deg,#6b7442 0,#9c8f5c 28%,#c1a06e 60%,#b89364)}
  .photo-progress{background:radial-gradient(ellipse at 55% 60%,#8a6a5c 0,#7d8792 45%,transparent 75%),linear-gradient(180deg,#c9c3b1 0,#a9aaa2 22%,#7c8b96 55%,#6f7f8a)}
  .photo-inspiration{background:radial-gradient(ellipse at 65% 55%,#5a5a5a 0,#7a7a7a 30%,transparent 60%),linear-gradient(180deg,#dadada 0,#b4b4b4 30%,#8c8c8c 60%,#7a7a7a)}

  .hero-photo{left:130px;top:-4px;width:620px;height:49px;background:linear-gradient(90deg,#3a2a22,#6b4631 45%,#2b211c 70%,#9fb7a0)}
  .signup-button{left:810px;top:-6px;width:219px;height:20px;background:var(--accent-orange);border-radius:0 0 3px 3px;box-shadow:0 1px 1px rgba(0,0,0,.3)}
  .section-rule{left:130px;top:95px;width:940px;height:0;border-top:1px solid var(--rule-dark);border-bottom:1px solid #d8dbdc}

  .rider-icon{background:var(--navy);border-radius:3px}
  .feature-title{font-family:"Noto Serif",serif;font-size:37px;line-height:1;color:var(--navy);font-weight:400}
  .feature-sub{font-family:"Noto Serif",serif;font-size:17.5px;line-height:22px;color:var(--navy);white-space:nowrap}
  .heading-rule{height:3px;background:var(--rule-light)}
  .feature-text{width:302px;font-size:14.4px;line-height:24px;letter-spacing:-.15px;color:var(--body-text)}
  .feature-text a{color:var(--link-rust);text-decoration:none}

  .benefits-panel{left:770px;top:144px;width:300px;height:527px;background:var(--panel-bg);border:2px solid #e2e4e5;box-shadow:0 1px 2px rgba(0,0,0,.2)}
  .benefits-title{left:20px;top:27px;font-family:"Noto Serif",serif;font-size:36.5px;line-height:36px;color:var(--navy);font-weight:400}
  .benefits-lead{left:20px;top:112px;width:250px;font-family:"Noto Serif",serif;font-size:14.6px;line-height:24px;color:var(--navy)}
  .benefits-rule{left:20px;top:223px;width:254px;height:2px;background:var(--rule-light)}
  .benefits-list{left:20px;top:244px;list-style:none;font-size:14.4px;line-height:24px;letter-spacing:-.15px;white-space:nowrap}

  .update-title{left:770px;top:710px;font-family:"Noto Serif",serif;font-size:36.5px;line-height:1;color:var(--navy);font-weight:400}
  .update-sub{left:770px;top:761px;font-family:"Noto Serif",serif;font-size:17.5px;color:var(--navy)}
  .update-rule{left:770px;top:787px;width:300px;height:3px;background:var(--rule-light)}
  .avatar{left:770px;top:815px;width:118px;height:100px;background:radial-gradient(ellipse at 50% 45%,#9a9a9a 0,#5a5a5a 50%,#222 100%)}
  .post-meta{left:909px;top:827px;font-size:11.5px;color:#333;white-space:nowrap}
  .post-meta .author{color:var(--navy)}
  .post-body{left:909px;top:851px;width:162px;font-size:11.5px;line-height:18px;color:#444}
</style>
</head>
<body>
  <div class="abs photo hero-photo" role="img" aria-label="Photo of a rider with a brown horse"></div>
  <div class="abs signup-button"></div>
  <div class="abs section-rule"></div>

  <!-- Fun -->
  <div class="abs rider-icon" style="left:136px;top:134px;width:64px;height:64px" role="img" aria-label="Galloping horse and rider icon"></div>
  <h2 class="abs feature-title" style="left:225px;top:137px">Fun</h2>
  <p class="abs feature-sub" style="left:225px;top:186px">Connect With Fun</p>
  <div class="abs heading-rule" style="left:130px;top:212px;width:300px"></div>
  <div class="abs photo photo-fun" style="left:130px;top:228px;width:300px;height:168px" role="img" aria-label="Photo of a smiling rider between two horses"></div>
  <p class="abs feature-text" style="left:129px;top:414px">You'll have social walls for you and your horse(s) to share your updates and training progress with others. Choose the humans and horses you want to follow, including Rowan and Tess's horses! Use our exclusive member locators to organize rides or to find a Brindlecott Instructor in your area.</p>

  <!-- Learning -->
  <div class="abs rider-icon" style="left:466px;top:134px;width:42px;height:70px" role="img" aria-label="Standing horse and rider icon"></div>
  <h2 class="abs feature-title" style="left:524px;top:137px">Learning</h2>
  <p class="abs feature-sub" style="left:524px;top:186px">Connect With Learning</p>
  <div class="abs heading-rule" style="left:450px;top:212px;width:300px"></div>
  <div class="abs photo photo-learning" style="left:450px;top:228px;width:300px;height:168px" role="img" aria-label="Photo of an instructor leading a young rider on a white horse"></div>
  <p class="abs feature-text" style="left:449px;top:414px">As a Brindlecott Member you will enjoy unlimited streaming video access to the complete Level 1 <a href="#">Education Program</a> from your com­puter or mobile device 24/7. You also have access to a wide range of Brindlecott educational videos, curated and provided to suit your level.</p>

  <!-- Progress -->
  <div class="abs rider-icon" style="left:132px;top:618px;width:60px;height:66px" role="img" aria-label="Trotting horse and rider icon"></div>
  <h2 class="abs feature-title" style="left:218px;top:616px">Progress</h2>
  <p class="abs feature-sub" style="left:217px;top:665px">Connect with Progress</p>
  <div class="abs heading-rule" style="left:130px;top:691px;width:300px"></div>
  <div class="abs photo photo-progress" style="left:130px;top:708px;width:300px;height:168px" role="img" aria-label="Photo of a toy horse racing game"></div>

  <!-- Inspiration -->
  <div class="abs rider-icon" style="left:452px;top:620px;width:62px;height:64px" role="img" aria-label="Horse and rider icon"></div>
  <h2 class="abs feature-title" style="left:535px;top:616px">Inspiration</h2>
  <p class="abs feature-sub" style="left:534px;top:665px">Connect with Inspiration</p>
  <div class="abs heading-rule" style="left:450px;top:691px;width:300px"></div>
  <div class="abs photo photo-inspiration" style="left:450px;top:708px;width:300px;height:168px" role="img" aria-label="Black and white photo of a horse running in a field"></div>

  <!-- Benefits -->
  <aside class="abs benefits-panel">
    <h2 class="abs benefits-title">Packed With<br>Benefits</h2>
    <p class="abs benefits-lead">Membership includes on-demand streaming access to the entire Level 1 Educational Content ($99 value)</p>
    <div class="abs benefits-rule"></div>
    <ul class="abs benefits-list">
      <li>Unlimited Access to Brindlecott Connect</li>
      <li>A Wall for You</li>
      <li>A Wall for Your Horse</li>
      <li>Interactive To-Do Lists</li>
      <li>Member Locator</li>
      <li>Personal Access to Rowan &amp; Tess</li>
      <li>Stride Notes Magazine</li>
      <li>Member Exclusive DVDs</li>
      <li>25% Merchandise Discount</li>
      <li>25% Off Event Tickets</li>
    </ul>
  </aside>

  <!-- Latest update -->
  <h2 class="abs update-title">Latest Update</h2>
  <p class="abs update-sub">From The community</p>
  <div class="abs update-rule"></div>
  <div class="abs photo avatar" role="img" aria-label="Black and white portrait of a community member in a hat"></div>
  <p class="abs post-meta"><span class="author">Dale Hartwick</span>, on 29 Feb 2012</p>
  <p class="abs post-body">Morbi leo risus, porta ac consectetur ac, vestibulum at eros.</p>
</body>
</html>
```